Plumbing & Heating bussiness card design

i do all plumbing and heating work and need a catchy design. keep it simple but eye catching nothing gimicky
i do 24hr call outs
landlord safety checks
all aspects of plumbing and heating
boiler breakdowns
flue sure reg number 648197
i have put up my old card. not to bothered about the front but i have put up the back for the details. mobile number and office are the same and the email has changed to dantapfixer@brevomail.net

Industry/Entity Type

Safety

Contact Information for Business Card

i do 24hr call outs
landlord safety checks
boiler breakdowns

Requirements
Must have
• i do 24hr call outs
• landlord safety checks
• all aspects of plumbing and heating
• boiler breakdowns
• flue sure reg number 648197

```html
<!DOCTYPE html>
<html lang="en">
<head>
<meta charset="utf-8">
<title>D Tapley Plumbing &amp; Heating – Business Card</title>
<link href="https://fonts.googleapis.com/css2?family=Open+Sans:ital,wght@0,400;0,600;0,700;1,400&display=swap" rel="stylesheet">
<style>
  :root {
    --page-bg: #e9e7e3;
    --card-white: #ffffff;
    --card-dark: #34353b;
    --accent-blue: #2a8fd6;
    --accent-red: #d42d3f;
    --badge-yellow: #f5d800;
    --text-dark: #3a3b40;
    --text-light: #f2f2f2;
    --text-muted: #c9cacd;
  }
  * { box-sizing: border-box; margin: 0; padding: 0; }
  html, body {
    width: 1200px; height: 950px; overflow: hidden;
    background: var(--page-bg);
    font-family: 'Open Sans', Arial, sans-serif;
  }
  .sheet {
    width: 1200px; height: 950px;
    display: flex; flex-direction: column; align-items: center; justify-content: center;
    gap: 34px;
  }
  .card {
    position: relative;
    width: 740px; height: 423px;
    overflow: hidden;
    box-shadow: 0 6px 18px rgba(0,0,0,0.18);
  }
  .card-front { background: var(--card-white); }
  .card-back { background: var(--card-dark); }
  .front-shapes { position: absolute; inset: 0; width: 100%; height: 100%; }

  .brand { position: absolute; display: flex; align-items: center; gap: 16px; }
  .brand-dot { width: 54px; height: 54px; border-radius: 50%; background: var(--accent-blue); flex: none; }
  .brand-name { font-weight: 600; line-height: 1.05; text-transform: uppercase; }
  .brand-name .line-main { display: block; font-size: 46px; letter-spacing: 1px; }
  .brand-name .line-sub { display: block; font-size: 21px; letter-spacing: 0.5px; }

  .card-front .brand { left: 46px; top: 196px; }
  .card-front .brand-name { color: var(--text-dark); }
  .card-front .brand-name .line-sub { color: var(--accent-blue); }

  .cert {
    position: absolute; left: 318px; top: 16px;
    display: flex; flex-direction: column; align-items: center; gap: 3px;
  }
  .cert-badge { width: 40px; height: 40px; background: var(--badge-yellow); }
  .cert-number { font-size: 11px; font-weight: 600; color: var(--text-dark); letter-spacing: 0.3px; }

  .contact {
    position: absolute; right: 40px; top: 70px;
    text-align: right; color: var(--text-muted);
    font-size: 15px; line-height: 1.6;
  }
  .contact-name { color: var(--accent-blue); font-weight: 600; font-size: 19px; letter-spacing: 1px; margin-bottom: 6px; }
  .contact-row { display: flex; justify-content: flex-end; align-items: center; gap: 8px; }
  .contact-row svg { width: 14px; height: 14px; fill: var(--accent-blue); }
  .contact-email { margin-top: 14px; }

  .card-back .brand { left: 46px; top: 44px; }
  .card-back .brand-dot { width: 46px; height: 46px; }
  .card-back .brand-name { color: var(--text-light); }
  .card-back .brand-name .line-main { font-size: 40px; }
  .card-back .brand-name .line-sub { font-size: 18px; color: var(--accent-red); }

  .services {
    position: absolute; left: 340px; top: 150px;
    list-style: none; color: var(--text-light);
    font-style: italic; font-size: 16px; line-height: 1.55;
  }
  .services li { display: flex; align-items: center; gap: 12px; }
  .services li::before {
    content: ""; width: 7px; height: 7px; border-radius: 50%;
    background: var(--accent-blue); flex: none;
  }
</style>
</head>
<body>
<main class="sheet">

  <section class="card card-front" aria-label="Card front">
    <svg class="front-shapes" viewBox="0 0 740 423" preserveAspectRatio="none" aria-hidden="true">
      <path d="M480 0 C410 40 400 110 404 170 C408 250 365 310 285 360 C245 385 220 405 205 423 L740 423 L740 0 Z" fill="var(--card-dark)"/>
      <path d="M505 -4 C430 24 388 75 389 150" fill="none" stroke="var(--accent-blue)" stroke-width="9"/>
      <path d="M318 348 C262 382 225 400 198 428" fill="none" stroke="var(--accent-red)" stroke-width="10"/>
    </svg>
    <div class="cert">
      <div class="cert-badge" aria-hidden="true"></div>
      <div class="cert-number">648197</div>
    </div>
    <div class="brand">
      <span class="brand-dot" aria-hidden="true"></span>
      <span class="brand-name">
        <span class="line-main">D Tapley</span>
        <span class="line-sub">Plumbing &amp; Heating</span>
      </span>
    </div>
    <div class="contact">
      <div class="contact-name">DAN</div>
      <div>42 Holloway Rd</div>
      <div>Exeter, EX2 4LN</div>
      <div class="contact-row">01632 960431
        <svg viewBox="0 0 24 24"><path d="M6.6 10.8a15 15 0 006.6 6.6l2.2-2.2a1 1 0 011-.25 11.4 11.4 0 003.6.6 1 1 0 011 1V20a1 1 0 01-1 1A17 17 0 013 4a1 1 0 011-1h3.5a1 1 0 011 1c0 1.250.2 2.450.6 3.6a1 1 0 01-.25 1z"/></svg>
      </div>
      <div class="contact-row">07700 900582
        <svg viewBox="0 0 24 24"><path d="M7 1h10a2 2 0 012 2v18a2 2 0 01-2 2H7a2 2 0 01-2-2V3a2 2 0 012-2zm0 3v14h10V4zm5 15.5a1 1 0 100 2 1 1 0 000-2z"/></svg>
      </div>
      <div class="contact-email">dantapfixer@brevomail.net</div>
    </div>
  </section>

  <section class="card card-back" aria-label="Card back">
    <div class="brand">
      <span class="brand-dot" aria-hidden="true"></span>
      <span class="brand-name">
        <span class="line-main">D Tapley</span>
        <span class="line-sub">Plumbing &amp; Heating</span>
      </span>
    </div>
    <ul class="services">
      <li>All aspects of Plumbing &amp; Heating</li>
      <li>24hr call outs</li>
      <li>Water regs approved</li>
      <li>Landlord safety checks</li>
      <li>Heating installation</li>
      <li>Boiler breakdowns</li>
      <li>Gas Safety Checks</li>
      <li>General Plumbing</li>
      <li>Bathrooms</li>
      <li>Renewables</li>
    </ul>
  </section>

</main>
</body>
</html>
```